Graphic design of labels for scented candles

Following a change in our team structure, a deadline was put in place and the brief changed.
We need a beautiful label for our candles, one that sticks *all around the glass*. Must obviously include our logo as well as the description of the perfume.
The clientele is mainly female, between 35 and 65 years old, of a classic nature.
Brand values:
Feminine
Warm-joyful
Sophisticated-elegant
Eco-friendly, pet-friendly
Natural
Inspires confidence.
The idea is to have something different, the final appearance must be elegant and refined, which will be your challenge given the shape.

What we need:
- changeable colors
- small transparent elements which can be printed on a gold or silver paper background (example: logo, frame, elements, etc.)

- the logo (black or very dark gray) must be present + text "vegetable candle", then the perfume and below:
vegetable wax - handcrafted"
I am attaching a picture of our current labels to the files.
For the size I'll let you manage.
These labels can also be assigned to derived products such as room fragrances, pillow mists, etc.
The brand targets the middle class and above.
For the fonts I leave the choice to you.
Thank you and good luck to all !

Update: there is no longer a cat's head as a background shape, you have free choice.
THANKS

Target Market(s)

Women aged 35 to 65

Industry/Entity Type

Industrie du Parfum

Colors
00AB8E
00BBA5
67D7C9
C6EFE9
E9F9F6
59FF00
82FF00
B8FF75
E3FFCB
F4FFEA
FFF300
FFF600
FEFA6F
FFFEC7
FFFEE8
FFC000
F8CF3A
FAE287
FDF2CF
FEFAEE
F0912C
F2A743
F7CA91
FBE8D2
FDF5EE
EE7325
F08F49
F5BC92
FAE3D3
FDF4ED
EB3D1F
EC4F4E
F09395
F8D3D4
FCEDEE
E54698
E96AAD
F1A4CE
F9D9EA
FCEFF6
A7469A
B969AE
D3A5CF
EDDBEB
F8F0F9
6B429C
8869AF
B7A5CE
E3DAEB
F3F0F8

Requirements
Must have
• modifiable colors - small transparent elements which can be printed on a gold or silver paper background (example: frame, elements, etc.) - the logo (black or very dark gray) must be present + text "vegetable candle, then the perfume and below: vegetable wax - handcrafted"
Nice to have
• Elements that could be made transparent (logo text frame) to be able to edit on gold papers and give a luxurious appearance
Should not have
• no childish appearance.

```html
<!DOCTYPE html>
<html lang="fr">
<head>
<meta charset="utf-8">
<title>Lumen Candle – Selva label</title>
<link rel="stylesheet" href="https://fonts.googleapis.com/css2?family=Cinzel:wght@400&family=Raleway:wght@300&display=swap">
<style>
  :root {
    --page-bg: #e6e6e6;
    --label-bg: #ffffff;
    --gold: #c9a24a;
    --gold-light: #f1dc9a;
    --gold-dark: #a57f2c;
    --ink: #2e2e2e;
    --rose: #d99693;
    --rose-light: #e7aaa6;
  }
  * { margin: 0; padding: 0; box-sizing: border-box; }
  html, body { width: 800px; height: 1200px; overflow: hidden; }
  body {
    background: radial-gradient(ellipse at center, #f4f4f4 0%, var(--page-bg) 100%);
    position: relative;
  }
  .label {
    position: absolute;
    left: 100px;
    top: 350px;
    width: 600px;
    height: 500px;
  }
  .label-frame {
    position: absolute;
    inset: 0;
    width: 600px;
    height: 500px;
  }
  .brand {
    position: absolute;
    top: 128px;
    left: 0;
    width: 100%;
    display: flex;
    justify-content: center;
    align-items: center;
    gap: 12px;
    font-family: "Cinzel", serif;
    font-size: 30px;
    color: var(--ink);
    letter-spacing: 3px;
  }
  .brand-dot {
    width: 12px;
    height: 12px;
    border-radius: 50%;
    background: var(--ink);
  }
  .perfume-name {
    position: absolute;
    top: 218px;
    left: 0;
    width: 100%;
    text-align: center;
    font-family: "Cinzel", serif;
    font-weight: 400;
    font-size: 100px;
    line-height: 1;
    color: var(--rose);
    letter-spacing: 1px;
  }
  .description {
    position: absolute;
    top: 385px;
    left: 0;
    width: 100%;
    text-align: center;
    font-family: "Raleway", sans-serif;
    font-weight: 300;
    font-size: 18px;
    line-height: 34px;
    color: var(--rose-light);
    letter-spacing: 0.5px;
  }
</style>
</head>
<body>
  <section class="label">
    <svg class="label-frame" viewBox="0 0 600 500" xmlns="http://www.w3.org/2000/svg">
      <defs>
        <linearGradient id="gold-foil" x1="0" y1="0" x2="1" y2="1">
          <stop offset="0" stop-color="#f1dc9a"/>
          <stop offset="0.5" stop-color="#c9a24a"/>
          <stop offset="1" stop-color="#a57f2c"/>
        </linearGradient>
      </defs>
      <path class="frame-line"
            d="M6 40 Q300 -30 594 40 L590 440 Q300 530 10 446 Z"
            fill="var(--label-bg)" stroke="url(#gold-foil)" stroke-width="2.5"/>
    </svg>

    <div class="brand"><span class="brand-dot"></span>Lumen Candle</div>

    <h1 class="perfume-name">SELVA</h1>

    <p class="description">BOUGIE PARFUMEE ARTISANALE<br>CIRE VEGETALE</p>
  </section>
</body>
</html>
```